Real Estate Brokerage Stationery Designs

I am looking to have presentation folders with business card slots on both sides along with pockets on both sides. I've attached logos, website colors along with current business card designs.

I am looking for envelope designs both big and small. Possibly new business card designs, notepad templates for big and small notepads. Letterhead designs. Pop socket designs. Realtors name badge designs.

www.tallbrookhomes.example

```html
<!DOCTYPE html>
<html lang="en">
<head>
<meta charset="utf-8">
<title>Tallbrook Homes – Business Card</title>
<link href="https://fonts.googleapis.com/css2?family=Roboto:wght@400;500;700&display=swap" rel="stylesheet">
<style>
  :root {
    --brand-blue: #0b56a8;
    --ink: #222222;
    --text-grey: #4a4a4a;
    --card-white: #ffffff;
    --backdrop: #9c9c9c;
    --badge-grey: #2b2b2b;
  }
  * { box-sizing: border-box; margin: 0; padding: 0; }
  html, body { width: 1133px; height: 1200px; overflow: hidden; }
  body {
    background: var(--backdrop);
    font-family: "Roboto", Arial, sans-serif;
    position: relative;
  }
  .card {
    position: absolute;
    left: 217px;
    width: 698px;
    height: 398px;
    background: var(--card-white);
    overflow: hidden;
  }
  .card--front { top: 153px; }
  .card--back { top: 647px; }

  /* Front */
  .accent-bar {
    position: absolute; left: 0; top: 50px;
    width: 12px; height: 46px;
    background: var(--brand-blue);
  }
  .agent-name {
    position: absolute; left: 41px; top: 48px;
    font-size: 26px; font-weight: 700; color: var(--brand-blue);
    letter-spacing: 0.2px;
  }
  .agent-title {
    position: absolute; left: 41px; top: 79px;
    font-size: 18px; font-weight: 500; color: var(--ink);
  }
  .office-address {
    position: absolute; left: 42px; top: 190px;
    font-size: 16.5px; line-height: 22px; color: var(--text-grey);
  }
  .contact-list {
    position: absolute; left: 42px; top: 251px;
    width: 258px;
    list-style: none;
  }
  .contact-list li {
    display: flex; align-items: center;
    height: 22px; font-size: 16.5px; color: var(--text-grey);
    white-space: nowrap;
  }
  .contact-list svg {
    flex: none;
    width: 16px; height: 16px; margin-right: 11px; fill: var(--brand-blue);
  }
  .portrait {
    position: absolute; right: 0; top: 0;
    width: 392px; height: 398px;
    background: linear-gradient(170deg, #f2f2f2 0%, #e4e4e4 40%, #6b5a50 62%, #2a2a2c 100%);
  }

  /* Back */
  .brand-mark {
    position: absolute; left: 0; right: 0; top: 180px;
    display: flex; justify-content: center; align-items: center; gap: 12px;
  }
  .brand-mark .brand-square {
    width: 22px; height: 22px; background: var(--brand-blue);
  }
  .brand-mark .brand-name {
    font-size: 38px; font-weight: 700; color: var(--ink);
  }
  .services {
    position: absolute; left: 0; right: 0; top: 324px;
    text-align: center; font-size: 17.5px; line-height: 22px; color: var(--text-grey);
  }
  .services .dot {
    display: inline-block; width: 6px; height: 6px;
    background: var(--brand-blue); margin: 0 6px; vertical-align: middle;
  }
  .badge-housing {
    position: absolute; left: 24px; top: 330px;
    width: 52px; height: 50px; background: var(--badge-grey);
  }
  .badge-listing {
    position: absolute; left: 587px; top: 328px;
    width: 84px; height: 42px; border: 2px solid var(--badge-grey);
  }
</style>
</head>
<body>

<section class="card card--front">
  <div class="accent-bar"></div>
  <h1 class="agent-name">Marcus Ellery</h1>
  <p class="agent-title">Broker</p>

  <p class="office-address">820 Harbor Point Dr, Suite 140,<br>Lakeview, FL 33011</p>

  <ul class="contact-list">
    <li>
      <svg viewBox="0 0 24 24" aria-hidden="true"><path d="M6.6 10.8c1.4 2.8 3.8 5.1 6.6 6.6l2.2-2.2c.3-.3.7-.4 1-.2 1.1.4 2.3.6 3.6.6.6 0 1 .4 1 1V20c0 .6-.4 1-1 1C10.6 21 3 13.4 3 4c0-.6.4-1 1-1h3.5c.6 0 1 .4 1 1 0 1.3.2 2.5.6 3.6.1.3 0 .7-.2 1z"/></svg>
      555-201-4830
    </li>
    <li>
      <svg viewBox="0 0 24 24" aria-hidden="true"><path d="M7 1h10c1.1 0 2 .9 2 2v18c0 1.1-.9 2-2 2H7c-1.1 0-2-.9-2-2V3c0-1.1.9-2 2-2zm0 3v14h10V4H7zm5 15.5a1 1 0 100 2 1 1 0 000-2z"/></svg>
      555-201-7762
    </li>
    <li>
      <svg viewBox="0 0 24 24" aria-hidden="true"><path d="M7 2h8l3 3v5H7V2zm-3 9h16c1.1 0 2 .9 2 2v6H2v-6c0-1.1.9-2 2-2zm2 10h12v2H6v-2z"/></svg>
      555-201-9105
    </li>
    <li>
      <svg viewBox="0 0 24 24" aria-hidden="true"><path d="M2 5h20v14H2V5zm2 2v.5l8 5 8-5V7H4z"/></svg>
      me@tallbrookhomes.example
    </li>
    <li>
      <svg viewBox="0 0 24 24" aria-hidden="true"><path d="M12 2a10 10 0 100 20 10 10 0 000-20zm-1 17.9A8 8 0 014.1 10L9 15v1c0 1.1.9 2 2 2v1.9zm6.9-2.5c-.3-.8-1-1.4-1.9-1.4h-1v-3c0-.6-.4-1-1-1H8v-2h2c.6 0 1-.4 1-1V7h2c1.1 0 2-.9 2-2v-.4a8 8 0 012.9 12.8z"/></svg>
      www.tallbrookhomes.example
    </li>
  </ul>

  <div class="portrait" role="img" aria-label="Portrait photograph of the broker in a dark suit and tie against a light backdrop"></div>
</section>

<section class="card card--back">
  <div class="brand-mark">
    <span class="brand-square"></span>
    <span class="brand-name">Tallbrook Homes</span>
  </div>

  <p class="services">
    Residential Real Estate<span class="dot"></span>Commercial Real Estate<br>
    Property Management<span class="dot"></span>Investments
  </p>

  <div class="badge-housing" role="img" aria-label="Fair housing badge"></div>
  <div class="badge-listing" role="img" aria-label="Listing service membership badge"></div>
</section>

</body>
</html>
```